Business card design needed

We are a smash repair business and have been in operation for almost 10 years. We have always had a card with a solid yellow background and black car door as a logo. We don't want to stray too far from this as all of our advertising incorporates same.

We do not wish to have anything comical or too wordy.

Industry/Entity Type

Advertising

Contact Information for Business Card

Derek & Marnie Tollard
Ridgewater Crash Works
Bays 21-25 Kestrel Crescent
Brackenvale NSW 2450
02 6573 2817
0428 316 752
office@ridgewatercrashworks.com.au

Logo Text

Ridgewater Crash Works

Logo styles of interest
Emblem Logo

```html
<!DOCTYPE html>
<html lang="en">
<head>
<meta charset="utf-8">
<title>Ridgewater Crash Works – Business Card</title>
<link rel="stylesheet" href="https://fonts.googleapis.com/css2?family=Questrial&display=swap">
<style>
  :root {
    --yellow: #f6d300;
    --yellow-deep: #eec400;
    --charcoal: #3b3b3d;
    --card-white: #f4f4f4;
    --card-grey: #dcdcdc;
    --door-grey: #c4c4c4;
    --text-grey: #6e6e6e;
    --name-grey: #5a5a5a;
    --backdrop: #e6e4e0;
  }
  * { margin: 0; padding: 0; box-sizing: border-box; }
  html, body { width: 1200px; height: 724px; overflow: hidden; }
  body {
    background: var(--backdrop);
    font-family: "Questrial", sans-serif;
    display: flex;
    align-items: center;
    justify-content: center;
    gap: 60px;
  }
  .card {
    position: relative;
    width: 520px;
    height: 317px;
    border-radius: 20px;
    overflow: hidden;
    box-shadow: 0 10px 28px rgba(0,0,0,0.18);
  }

  /* Front */
  .card-front {
    background: linear-gradient(135deg, var(--yellow) 0%, var(--yellow-deep) 100%);
  }
  .brand {
    position: absolute;
    left: 50%;
    top: 50%;
    transform: translate(-50%, -50%);
    display: flex;
    align-items: center;
    gap: 16px;
    color: var(--charcoal);
    font-size: 30px;
    white-space: nowrap;
  }
  .brand-mark {
    width: 26px;
    height: 26px;
    background: var(--charcoal);
  }
  .front-web {
    position: absolute;
    right: 14px;
    top: 50%;
    transform: translateY(-50%);
    writing-mode: vertical-rl;
    font-size: 10px;
    color: var(--charcoal);
    white-space: nowrap;
  }

  /* Back */
  .card-back {
    background: linear-gradient(135deg, #fafafa 0%, var(--card-white) 55%, var(--card-grey) 100%);
  }
  .back-mark {
    position: absolute;
    right: 26px;
    top: 30px;
    font-size: 30px;
    color: var(--door-grey);
    white-space: nowrap;
  }
  .contact {
    position: absolute;
    left: 34px;
    top: 148px;
    color: var(--text-grey);
  }
  .contact-name {
    font-size: 24px;
    color: var(--name-grey);
    margin-bottom: 12px;
  }
  .contact-line {
    font-size: 12px;
    line-height: 1.45;
  }
  .back-rule {
    position: absolute;
    left: 0;
    right: 0;
    bottom: 38px;
    height: 6px;
    background: var(--charcoal);
  }
  .back-band {
    position: absolute;
    left: 0;
    right: 0;
    bottom: 0;
    height: 38px;
    background: linear-gradient(90deg, var(--yellow), #f8b800);
    display: flex;
    align-items: center;
    justify-content: flex-end;
    padding-right: 34px;
  }
  .band-name {
    font-size: 15px;
    color: var(--charcoal);
  }
</style>
</head>
<body>
  <section class="card card-front" aria-label="Card front">
    <div class="brand">
      <span class="brand-mark"></span>
      <span class="brand-name">Ridgewater Crash Works</span>
    </div>
    <p class="front-web">ridgewatercrashworks.com.au</p>
  </section>

  <section class="card card-back" aria-label="Card back">
    <p class="back-mark">Ridgewater Crash Works</p>
    <div class="contact">
      <p class="contact-name">Derek &amp; Marnie Tollard</p>
      <p class="contact-line">Bays 21-25 Kestrel Crescent Brackenvale NSW 2450</p>
      <p class="contact-line">02 6573 2817 &nbsp; 0428 316 752</p>
      <p class="contact-line">office@ridgewatercrashworks.com.au</p>
    </div>
    <div class="back-rule"></div>
    <div class="back-band">
      <span class="band-name">Ridgewater Crash Works</span>
    </div>
  </section>
</body>
</html>
```